Great Pie Give Away

I am a Realtor and will be Mailing this Postcard to my best Clients Inviting them to Select the Pie they want for Thanksgiving and I will open my office for them to pick up. here's my thought on text:

THANK YOU GREAT PIE GIVE AWAY!
Tues Nov 25th 3 to 8PM

In Giving Thanks for Your Support and Referrals I want to Personally Invite You to My 1st Annual "Great Pie Giveaway". You have a choice of:
*Apple
*Pumpkin
*Pecan

Please let me know Your Choice by Mon Nov 17th. Please Feel Free to email me or Call Me with Your Pie Choice!

There will be Food and Drink Including My Award Winning Chili.

417 Birch Lane
Dunmore Me 04217
wade@wadeholloran.net
207.381.5964

Please Give it a Thanksgiving Look....I did not include a photo of a pie but open to it. PLEASE make the Paragraph "In Giving Thanks with the 3 Pie choices the Focal Point that Draws Your eyes to it.

```html
<!DOCTYPE html>
<html lang="en">
<head>
<meta charset="utf-8">
<title>Thank You – Great Pie Give Away</title>
<link rel="stylesheet" href="https://fonts.googleapis.com/css2?family=Righteous&family=Cinzel:wght@400;700&display=swap">
<style>
  :root {
    --sun: #fff6c8;
    --gold: #ffd23a;
    --amber: #f7a81b;
    --orange: #ef8a12;
    --rust: #c9641a;
    --maroon: #8c2838;
    --maroon-dark: #4f0f1a;
    --cream: #fff3d8;
    --leaf-light: #f6b845;
    --leaf-deep: #d9751a;
    --pumpkin: #f28c1c;
    --crust: #e7a35a;
    --cloud: #fff1cf;
  }
  html, body {
    margin: 0;
    padding: 0;
    overflow: hidden;
    background: #ffffff;
  }
  .postcard {
    position: relative;
    width: 1200px;
    height: 938px;
    overflow: hidden;
    background:
      radial-gradient(ellipse 55% 40% at 40% 18%, var(--sun) 0%, rgba(255,246,200,0) 70%),
      radial-gradient(ellipse 70% 50% at 60% 55%, #ffe79a 0%, rgba(255,231,154,0) 75%),
      linear-gradient(180deg, #fde08a 0%, var(--gold) 28%, var(--amber) 55%, var(--orange) 100%);
  }
  .bokeh {
    position: absolute;
    border-radius: 50%;
    background: rgba(255,255,255,0.55);
  }
  .foliage {
    position: absolute;
    left: 0;
    top: 410px;
    width: 1200px;
    height: 528px;
    background:
      radial-gradient(ellipse 40% 30% at 50% 10%, rgba(255,240,190,0.7) 0%, rgba(255,240,190,0) 100%),
      linear-gradient(180deg, rgba(246,184,69,0) 0%, var(--leaf-light) 30%, var(--leaf-deep) 100%);
  }
  .pumpkins {
    position: absolute;
    top: 750px;
    height: 188px;
    border-radius: 90px 90px 20px 20px;
    background: radial-gradient(ellipse at 50% 45%, #ffb347 0%, var(--pumpkin) 55%, #c9560c 100%);
  }
  .pumpkins--left { left: 270px; width: 220px; }
  .pumpkins--right { left: 700px; width: 210px; }
  .pie-slice {
    position: absolute;
    top: 248px;
    width: 140px;
    height: 66px;
    border-radius: 40px;
    background: radial-gradient(ellipse at 55% 45%, var(--crust) 0%, #c46a2a 45%, var(--cloud) 48%, var(--cloud) 100%);
  }
  .pie-slice--left { left: 175px; }
  .pie-slice--right { left: 860px; }

  .headline, .line {
    position: absolute;
    left: 0;
    width: 1200px;
    margin: 0;
    text-align: center;
    white-space: nowrap;
    text-transform: uppercase;
  }
  .headline {
    font-family: "Righteous", sans-serif;
    color: var(--maroon);
    -webkit-text-stroke: 2px var(--maroon-dark);
    text-shadow: 0 0 10px rgba(255,255,255,0.9), 0 3px 6px rgba(80,15,25,0.5);
  }
  .headline--thanks { top: 38px; font-size: 116px; line-height: 1; letter-spacing: 1px; }
  .headline--event { top: 152px; font-size: 58px; line-height: 1; }

  .event-date {
    top: 226px;
    font-family: "Cinzel", serif;
    font-weight: 700;
    font-size: 36px;
    color: #b8662a;
    text-shadow: 0 0 4px var(--maroon-dark);
    text-transform: none;
    font-variant: small-caps;
  }
  .focal {
    font-family: "Righteous", sans-serif;
    color: var(--amber);
    -webkit-text-stroke: 1px var(--maroon-dark);
    text-shadow: 0 0 6px rgba(110,30,10,0.85);
  }
  .focal--lead { top: 272px; font-size: 50px; }
  .focal--body { font-size: 27px; color: #f6a52a; }
  .focal--body-1 { top: 334px; }
  .focal--body-2 { top: 368px; }
  .focal--choice { top: 398px; font-size: 45px; color: var(--gold); }

  .pie-choices {
    position: absolute;
    left: 500px;
    top: 466px;
    margin: 0;
    padding: 0;
    list-style: none;
    font-family: "Cinzel", serif;
    font-weight: 700;
    font-size: 38px;
    line-height: 59px;
    color: var(--rust);
    font-variant: small-caps;
    text-shadow: 0 0 4px var(--maroon-dark), 0 0 10px rgba(255,240,200,0.8);
  }
  .pie-choices li::before { content: "*"; }

  .extras {
    top: 640px;
    font-family: "Righteous", sans-serif;
    font-size: 25px;
    color: var(--gold);
    text-shadow: 0 0 5px var(--maroon-dark);
  }
  .rsvp {
    font-family: "Righteous", sans-serif;
    font-size: 31px;
    color: var(--maroon);
    -webkit-text-stroke: 1px var(--maroon-dark);
    text-shadow: 0 0 6px rgba(255,220,120,0.9);
  }
  .rsvp--deadline { top: 680px; }
  .rsvp--contact { top: 724px; }

  .contact {
    position: absolute;
    left: 0;
    top: 772px;
    width: 1200px;
    margin: 0;
    text-align: center;
    font-family: "Cinzel", serif;
    font-weight: 400;
    font-style: normal;
    font-size: 20px;
    line-height: 24px;
    color: var(--cream);
    font-variant: small-caps;
    text-shadow: 0 0 3px var(--maroon-dark), 0 0 6px var(--maroon-dark);
  }
  .contact span { display: block; }
</style>
</head>
<body>
<main class="postcard">
  <span class="bokeh" style="left:30px;top:60px;width:90px;height:90px"></span>
  <span class="bokeh" style="left:120px;top:70px;width:70px;height:70px"></span>
  <span class="bokeh" style="left:40px;top:180px;width:60px;height:60px"></span>
  <span class="bokeh" style="left:410px;top:0;width:60px;height:40px"></span>
  <span class="bokeh" style="left:980px;top:10px;width:70px;height:70px"></span>
  <span class="bokeh" style="left:1050px;top:60px;width:100px;height:100px;opacity:.6"></span>
  <span class="bokeh" style="left:1085px;top:235px;width:70px;height:70px"></span>

  <div class="foliage" role="img" aria-label="Autumn maple leaves spread across the lower half"></div>
  <div class="pumpkins pumpkins--left" role="img" aria-label="Pumpkins with curling vines and leaves"></div>
  <div class="pumpkins pumpkins--right" role="img" aria-label="Pumpkins with curling vines and leaves"></div>
  <div class="pie-slice pie-slice--left" role="img" aria-label="Slice of pumpkin pie with whipped cream"></div>
  <div class="pie-slice pie-slice--right" role="img" aria-label="Slice of pumpkin pie with whipped cream"></div>

  <h1 class="headline headline--thanks">Thank You</h1>
  <h2 class="headline headline--event">Great Pie Give Away!</h2>
  <p class="line event-date">Tues Nov 25th 3-8 pm</p>

  <p class="line focal focal--lead">In Giving Thanks</p>
  <p class="line focal focal--body focal--body-1">For your support and referrals I want to</p>
  <p class="line focal focal--body focal--body-2">personally invite you to my 1st annual "Great Pie Giveaway".</p>
  <p class="line focal focal--choice">You have a choice of:</p>

  <ul class="pie-choices">
    <li>Apple</li>
    <li>Pumpkin</li>
    <li>Pecan</li>
  </ul>

  <p class="line extras">There will be food and drink including my award winning chili.</p>
  <p class="line rsvp rsvp--deadline">Please let me know your choice by Mon Nov 17th.</p>
  <p class="line rsvp rsvp--contact">Please feel free to email me or call me with your pie choice!</p>

  <address class="contact">
    <span>417 Birch Lane</span>
    <span>Dunmore Me 04217</span>
    <span>wade@wadeholloran.net</span>
    <span>207.381.5964</span>
  </address>
</main>
</body>
</html>
```